Lumen Heat Flow Studio – Corporate Brand Identity

We are in need of a full company image and brand identity design for a brand new hot yoga studio in a small but busy and wealthy oil town.
Our logo was designed through artfolkhub and we currently have an open wordpress project in artfolkhub with a deadline of July 14. We plan on continuing to build our marketing presence through artfolkhub or one on one with designers that have been able to capture our vision easily. So, there are many more opportunities for continued projects.
We love our current logo and would like it to be utilized well. We want our logo to be familiar, known and synonymous with hot yoga in Alberta, Canada. We have intentions of opening up more locations and are looking for a strong brand that we can eventually franchise.
We need to display a strong but serene image that demands awe and communicates to people that Lumen Heat Flow is the real deal and will provide them with exactly what they need. Our studio is the perfect balance of what you would gain from going to a gym and developing your physical fitness and visiting a spa and nurturing a quiet mind, calm spirit and finding relaxation. We are all of this in one place. Breathe. Bend. Beam. – Steady Frame. Still Thought. Soft Heart.
In every detail our brand image should feel that “we are it.. the real deal when it comes to yoga…the place you want to be… the community you want to be apart of”. We need to appeal to men and women and a very important part of our business will be offering corporate packages and workplace yoga to the large oil companies in town. Our clientele is affluent so although we want creativity it still needs to be posh and upscale.
Most importantly, we are looking for something that is extraordinarily creative and show stopping. We want to set ourselves apart from all other studios in Canada, in terms of our creative, beautiful print marketing. When I say innovative, I’m thinking outside the box as in we want to be known for having beautiful and creative brand image http://www.quirkmole.com/fitness-and-yoga-ads/ I also like the idea of utilizing an image of the most beautiful oasis – see http://markvaultstudio.com/prana-loft-geneva/
We are in need of at least the following:
- Business Cards – Front & Back
- Standard Letterhead (Size A4)
- Continuation Letterhead
- Envelopes (Sizes C4 & A4, , C5, DL)
- Postcard (for voucher, birthday, marketing)
- Loyalty Card design (front and back) for 10 visits
- Gift Certificate design
- Presentation Folder (for corporate packages)
- Standard Invoice A4 (word template)
- With Compliments Slips A5 (word template)
- Email Signature
OPTIONAL
- Labels for Branded Retail Products (Mat Spray, Room Spray, Aromatherapy)
- Social Media (Facebook Cover, etc)
All items must be editable in regards to changing names, addresses, etc. and high resolution please.
Please let me know if you require the logo in another format - ie. "ai, eps"

```html
<!DOCTYPE html>
<html lang="en">
<head>
<meta charset="utf-8">
<title>Lumen Heat Flow Studio – Stationery Set</title>
<link rel="stylesheet" href="https://fonts.googleapis.com/css2?family=Arimo:wght@400;700&family=Tinos&display=swap">
<style>
  :root {
    --teal: #3a9ea5;
    --teal-deep: #1f7f86;
    --rule: #2aa3b3;
    --ink: #2b2b2b;
    --ink-soft: #555;
    --paper: #ffffff;
    --edge: #c9c9c9;
    --flap: #b5b5b5;
    --window: #cfcfd1;
    --photo-sky: #dfeef0;
    --photo-haze: #9fb9b4;
    --photo-green: #4f7a4e;
    --photo-dark: #2f5233;
  }
  * { margin: 0; padding: 0; box-sizing: border-box; }
  html, body { width: 1200px; height: 779px; overflow: hidden; background: #fff; }
  body { position: relative; font-family: "Arimo", Arial, sans-serif; color: var(--ink); }

  .piece { position: absolute; background: var(--paper); border: 1px solid var(--edge); overflow: hidden; }

  .brand { position: absolute; display: flex; align-items: center; gap: 6px; color: var(--teal);
           font-family: "Arimo", Arial, sans-serif; font-weight: 400; white-space: nowrap; }
  .brand-dot { border-radius: 50%; background: var(--teal); flex: none; }
  .brand-sm { font-size: 12px; }
  .brand-sm .brand-dot { width: 14px; height: 14px; }
  .brand-xs { font-size: 11px; }
  .brand-xs .brand-dot { width: 12px; height: 12px; }
  .brand-md { font-size: 14px; }
  .brand-md .brand-dot { width: 18px; height: 18px; }

  .landscape { position: absolute; left: 0; right: 0; bottom: 0;
    background: linear-gradient(180deg, var(--photo-sky) 0%, var(--photo-haze) 22%, var(--photo-green) 55%, var(--photo-dark) 100%); }

  /* business cards */
  .card { top: 71px; width: 264px; height: 168px; }
  .card-front { left: 43px; }
  .card-front .brand { left: 66px; top: 18px; }
  .card-front .landscape { height: 98px; }
  .card-back { left: 367px; }
  .card-back .brand { left: 24px; top: 18px; }
  .card-name { position: absolute; left: 18px; top: 104px; font-weight: 700; font-size: 11px; color: var(--ink-soft); }
  .contact { position: absolute; font-size: 6.4px; line-height: 8.6px; color: var(--ink-soft); }
  .card-back .contact { left: 18px; top: 122px; }

  /* envelope */
  .env-flap { position: absolute; left: 33px; top: 300px; }
  .envelope { left: 33px; top: 335px; width: 565px; height: 284px; }
  .envelope .brand { left: 30px; top: 22px; }
  .envelope .contact { left: 26px; top: 68px; }
  .envelope .landscape { height: 178px; }
  .env-window { position: absolute; left: 28px; top: 187px; width: 159px; height: 48px; background: var(--window); border-radius: 7px; }

  /* letterhead */
  .letter { left: 685px; top: 36px; width: 475px; height: 671px; z-index: 1; }
  .letter .brand { right: 46px; top: 34px; }
  .letter-rule { position: absolute; left: 79px; top: 76px; width: 350px; height: 2px; background: var(--rule); }
  .letter-text { position: absolute; left: 84px; width: 340px; font-size: 8.3px; line-height: 11.6px; color: var(--ink); }
  .letter-text p + p { margin-top: 11px; }
  .addressee { top: 164px; }
  .dateline { top: 214px; }
  .salutation { top: 278px; }
  .body-copy { top: 296px; }
  .closing { top: 537px; font-family: "Tinos", "Times New Roman", serif; }
  .signature { position: absolute; left: 84px; top: 551px; width: 90px; height: 18px;
               background: linear-gradient(90deg, #bbb, #e8e8e8); border-radius: 9px; }
  .signer { top: 570px; font-family: "Tinos", "Times New Roman", serif; line-height: 10.5px; }
  .copies { top: 608px; font-family: "Tinos", "Times New Roman", serif; line-height: 11px; }

  /* disc – lies on top of the letterhead edge */
  .disc { position: absolute; left: 488px; top: 496px; width: 254px; height: 254px; border-radius: 50%;
          background: var(--paper); border: 1px solid #555; overflow: hidden; z-index: 2; }
  .disc-ring { position: absolute; border-radius: 50%; border: 1px solid #6c6c7a; }
  .disc .landscape { height: 105px; }
  .disc .brand { left: 0; right: 0; top: 36px; justify-content: center; }
  .disc-mark { position: absolute; left: 18px; top: 128px; width: 26px; height: 10px; border: 1px solid #999; }
</style>
</head>
<body>

<!-- business card front -->
<section class="piece card card-front">
  <div class="brand brand-sm"><span class="brand-dot"></span>Lumen Heat Flow Studio</div>
  <div class="landscape" role="img" aria-label="Photo of a quiet country road through green forest toward a distant mountain"></div>
</section>

<!-- business card back -->
<section class="piece card card-back">
  <div class="brand brand-sm"><span class="brand-dot"></span>Lumen Heat Flow Studio</div>
  <div class="card-name">COMPANYNAME</div>
  <div class="contact">
    Full Company Name<br>
    Address: Text text text text text text text text<br>
    Tel.:+00 000 000 00 00, fax.: +00 000 000 00 00<br>
    e-male: office@lumenflow.com
  </div>
</section>

<!-- envelope -->
<svg class="env-flap" width="565" height="36" viewBox="0 0 565 36" aria-hidden="true">
  <polygon points="0,36 38,0 527,0 565,36" fill="var(--flap)"/>
</svg>
<section class="piece envelope">
  <div class="brand brand-md"><span class="brand-dot"></span>Lumen Heat Flow Studio</div>
  <div class="contact">
    Full Company Name<br>
    Address: Text text text text text text text text text<br>
    Tel.:+00 000 000 00 00, fax.: +00 000 000 00 00<br>
    e-male: office@lumenflow.com
  </div>
  <div class="landscape" role="img" aria-label="Photo of a quiet country road through green forest toward a distant mountain"></div>
  <div class="env-window"></div>
</section>

<!-- letterhead -->
<section class="piece letter">
  <div class="brand brand-md"><span class="brand-dot"></span>Lumen Heat Flow Studio</div>
  <div class="letter-rule"></div>

  <div class="letter-text addressee">Domnul Numele Destinatarului,<br>Adresa Destinatarului<br>Oras, Judet Cod postal</div>
  <div class="letter-text dateline">Iasi, Ziua Luna, Anul</div>
  <div class="letter-text salutation">Domnului Numele Destinatarului,</div>
  <div class="letter-text body-copy">
    <p>Lorem ipsum dolor sit amet, consectetuer adipiscing elit, sed diam nonummy nibh euismod tincidunt ut laoreet dolore magna aliquam erat volutpat. Ut wisi enim ad minim veniam, quis nostrud exerci tation ullamcorper suscipit lobortis nisl ut aliquip ex ea commodo.</p>
    <p>Duis autem vel eum iriure dolor in hendrerit in vulputate velit esse molestie consequat, vel illum dolore eu feugiat nulla facilisis at vero eros et accumsan et iusto odio dignissim qui blandit praesent lup tatum zzril delenit augue duis scing elit, sed diam nonummy nibh euismod tincidunt ut laoreet dolore magna aliquam erat volutpat.</p>
    <p>Ut wisi enim ad minim veniam, quis nostrud exerci tation ullamcorper suscipit dolor in hendrerit in vulputate velit esse molestie consequat, vel illum dolore eu feugiat nulla facilisis at vero eros et accumsan et iusto odio dignissim qui blandit praesent luptatum zzril delenit augue duis dolore te feugait nulla facilisi. Ut laoreet dolore magna aliquam erat volutpat. Ut wisi enim ad minim veniam, quis nostrud exerci tation ullamcorper suscipit lobortis nisl ut aliquip ex ea commodo consequat.</p>
  </div>
  <div class="letter-text closing">Sincerely,</div>
  <div class="signature" role="img" aria-label="Handwritten signature"></div>
  <div class="letter-text signer">Daniel Marsh<br>Deputy Assistant Director</div>
  <div class="letter-text copies">Cc:&nbsp; R. Haldane<br>&nbsp;&nbsp;&nbsp;&nbsp;&nbsp;&nbsp;T. Corwin</div>
</section>

<!-- disc -->
<section class="disc">
  <div class="landscape" role="img" aria-label="Photo of a country road through green forest"></div>
  <div class="brand brand-xs"><span class="brand-dot"></span>Lumen Heat Flow Studio</div>
  <div class="disc-mark"></div>
  <div class="disc-ring" style="left:82px;top:82px;width:90px;height:90px;"></div>
  <div class="disc-ring" style="left:106px;top:106px;width:42px;height:42px;"></div>
</section>

</body>
</html>
```